Time for a new business card design

We need a new business card design for Torvel Furniture Rentals based in Australia. www.torvel-example.com.au. We specialise in providing furniture rentals for home staging, corporate relocations events and product launches etc. We would like to see designs that include our logo on the front of the card with all the standard contact details as well as having a realy nice image on the back with a list of our services we offer. Our logo is red and this cannot change. Were looking for a pallet of red and white with maybe a splash of grey. The final design should communication organised & stylish. We are in the process of finalising our new website and would like the card design to compliment this as well

Industry/Entity Type

Communication

Requirements
Must have
• Square corners
logo
name, title, email, phone, address
image on back of card with space for list of services we offer
Services:
•Furniture and appliance rental
•Property styling
•Events and functions
•Office furniture rental

The card must be landscape.
The image is to appear on the back of the card only.

```html
<!DOCTYPE html>
<html lang="en">
<head>
<meta charset="utf-8">
<title>Torvel Furniture Rentals – Business Card</title>
<link rel="stylesheet" href="https://fonts.googleapis.com/css2?family=Ubuntu:wght@300;400;700&display=swap">
<style>
  :root {
    --brand-red: #bd2029;
    --brand-red-light: #e07a7f;
    --card-white: #f4f5f7;
    --card-grey: #dfe1e5;
    --ink: #2b2b2b;
    --stage: #4d4d4d;
  }
  * { margin: 0; padding: 0; box-sizing: border-box; }
  html, body {
    width: 862px; height: 1200px; overflow: hidden;
    background: var(--stage);
    font-family: "Ubuntu", sans-serif;
  }
  .card {
    position: absolute; left: 57px;
    width: 747px; height: 483px;
    overflow: hidden; background: var(--card-white);
  }
  .card--front { top: 48px; }
  .card--back { top: 644px; }
  .card__art { position: absolute; inset: 0; width: 100%; height: 100%; }

  .logo-name {
    position: absolute; left: 44px; top: 72px;
    color: #fff; font-weight: 300; font-size: 31px; letter-spacing: -0.5px;
    white-space: nowrap;
  }
  .contact {
    position: absolute; left: 428px; top: 208px;
    color: #fff; font-weight: 700; font-size: 22px; line-height: 33px;
    list-style: none;
  }
  .website {
    position: absolute; left: 30px; top: 438px;
    color: var(--brand-red); font-weight: 700; font-size: 16px; letter-spacing: 0;
    white-space: nowrap;
  }

  .services { position: absolute; left: 456px; top: 138px; }
  .services__title {
    color: var(--brand-red); font-weight: 700; font-size: 18px; margin-bottom: 14px;
  }
  .services__list { list-style: none; }
  .services__list li {
    color: var(--ink); font-size: 17px; line-height: 42px;
  }
</style>
</head>
<body>

<section class="card card--front">
  <svg class="card__art" viewBox="0 0 501 324" preserveAspectRatio="none" aria-hidden="true">
    <path d="M0,110 C120,60 300,40 501,80" fill="none" stroke="#ffffff" stroke-width="10" opacity="0.7"/>
    <path d="M0,260 C100,180 180,120 260,0" fill="none" stroke="#e6e8ec" stroke-width="14" opacity="0.8"/>
    <path d="M0,324 L0,250 C90,230 160,270 200,324 Z" fill="var(--card-grey)" opacity="0.5"/>
    <path d="M219,0 Q140,160 212,324 L222,324 Q150,160 229,0 Z" fill="var(--brand-red-light)" opacity="0.6"/>
    <path d="M229,0 L501,0 L501,324 L222,324 Q150,160 229,0 Z" fill="var(--brand-red)"/>
    <rect x="15" y="16" width="240" height="100" fill="var(--brand-red)"/>
  </svg>
  <div class="logo-name">Torvel Furniture Rentals</div>
  <ul class="contact">
    <li>Name,</li>
    <li>title,</li>
    <li>email,</li>
    <li>phone,</li>
    <li>address</li>
  </ul>
  <div class="website">www.torvel-example.com.au</div>
</section>

<section class="card card--back">
  <svg class="card__art" viewBox="0 0 501 324" preserveAspectRatio="none">
    <defs>
      <linearGradient id="roomTones" x1="0" y1="0" x2="0" y2="1">
        <stop offset="0" stop-color="#6fa6d8"/>
        <stop offset="0.35" stop-color="#9fb4c6"/>
        <stop offset="0.55" stop-color="#d8d4cc"/>
        <stop offset="1" stop-color="#eef0f2"/>
      </linearGradient>
    </defs>
    <path d="M300,0 C380,100 440,200 501,260" fill="none" stroke="#ffffff" stroke-width="12" opacity="0.8"/>
    <path d="M260,40 C360,60 440,120 501,200" fill="none" stroke="#e3e5e9" stroke-width="8" opacity="0.8"/>
    <path d="M227,0 Q320,150 267,324 L279,324 Q334,150 239,0 Z" fill="var(--brand-red-light)" opacity="0.6"/>
    <path d="M0,0 L227,0 Q320,150 267,324 L0,324 Z" fill="var(--brand-red)"/>
    <path d="M0,0 L221,0 Q312,150 261,324 L0,324 Z" fill="url(#roomTones)"
          role="img" aria-label="Photo of a styled bright bedroom with a window, white bed, cushions and a bedside lamp"/>
  </svg>
  <div class="services">
    <h2 class="services__title">SERVICES</h2>
    <ul class="services__list">
      <li>Furniture and appliance rental</li>
      <li>Property styling</li>
      <li>Events and functions</li>
      <li>Office furniture rental</li>
    </ul>
  </div>
</section>

</body>
</html>
```